I need to create a product box

I need a designer for a candle-making kit. Attached please find the die-cut and some of the elements I will like to include in the box. Also, there is a sample box. I want the designer to know this is an ecofriendly product but the packaging needs to be classy, unisex and eye-catching.

file:///C:/Users/marvo/Downloads/Untitled%20design.svg

Colors
0054AA
0677BA
7BADD7
CADEEF
E8F1F8
0094D4
00A9DD
6FCCEA
C7EBF8
E9F6FB
00AB8E
00BBA5
67D7C9
C6EFE9
E9F9F6
FFF300
FFF600
FEFA6F
FFFEC7
FFFEE8
FFC000
F8CF3A
FAE287
FDF2CF
FEFAEE
F0912C
F2A743
F7CA91
FBE8D2
FDF5EE
A7469A
B969AE
D3A5CF
EDDBEB
F8F0F9

```html
<!DOCTYPE html>
<html lang="en">
<head>
<meta charset="utf-8">
<title>Ember Grove – Candle Making Kit Box</title>
<link rel="stylesheet" href="https://fonts.googleapis.com/css2?family=Josefin+Sans:wght@300;400&family=Cormorant+Garamond:wght@500&family=Parisienne&display=swap">
<style>
  :root {
    --backdrop: #e4d3f2;
    --lid: #efe9e8;
    --panel-green: #456b4d;
    --panel-text: #d9e4dc;
    --ink-green: #3f6b4f;
    --sage: #8aa897;
    --feature-grey: #a9b3ad;
  }
  * { margin: 0; padding: 0; box-sizing: border-box; }
  html, body { width: 1200px; height: 840px; overflow: hidden; background: var(--backdrop); }
  .canvas { position: relative; width: 1200px; height: 840px; }
  .box {
    position: absolute; left: 50px; top: 110px; width: 1100px; height: 620px;
    display: flex; box-shadow: 0 18px 40px rgba(110, 70, 150, 0.25);
  }
  .end-panel {
    position: relative; width: 150px; height: 100%;
    background: var(--panel-green); overflow: hidden;
  }
  .end-brand {
    position: absolute; left: 50%; top: 50%;
    transform: translate(-50%, -50%) rotate(90deg);
    white-space: nowrap; text-align: center; color: var(--panel-text);
  }
  .end-brand-name {
    font-family: "Josefin Sans", sans-serif; font-weight: 400;
    font-size: 34px; letter-spacing: 1px;
  }
  .end-brand-tagline {
    font-family: "Cormorant Garamond", serif; font-weight: 500;
    font-size: 10px; letter-spacing: 3px; margin-top: 4px;
  }
  .lid {
    position: relative; flex: 1; height: 100%;
    background: var(--lid); overflow: hidden;
  }
  .brand {
    position: absolute; right: 110px; top: 70px; text-align: center;
    color: var(--ink-green);
  }
  .brand-name {
    font-family: "Josefin Sans", sans-serif; font-weight: 400;
    font-size: 46px; letter-spacing: 1px; display: flex; align-items: center; gap: 12px;
  }
  .brand-dot { width: 14px; height: 14px; border-radius: 50%; background: var(--ink-green); }
  .brand-tagline {
    font-family: "Cormorant Garamond", serif; font-weight: 500;
    font-size: 11px; letter-spacing: 3px; margin-top: 4px;
  }
  .hero-illustration {
    position: absolute; left: 80px; top: 60px; width: 460px; height: 380px;
    background: linear-gradient(160deg, #e6e8e3 0%, #d7dfd8 55%, #e9e6e4 100%);
  }
  .features {
    position: absolute; left: 0; right: 0; top: 468px; text-align: center;
    font-family: "Josefin Sans", sans-serif; font-weight: 300; font-size: 17px;
    letter-spacing: 1px; color: var(--feature-grey);
  }
  .heart { position: absolute; left: 50%; top: 505px; transform: translateX(-50%); }
  .closing-note {
    position: absolute; left: 0; right: 0; top: 530px; text-align: center;
    font-family: "Parisienne", cursive; font-size: 30px; line-height: 38px;
    color: var(--ink-green);
  }
</style>
</head>
<body>
<div class="canvas">
  <div class="box">
    <aside class="end-panel" role="img" aria-label="Green end panel with faint line-drawn daisy pattern">
      <div class="end-brand">
        <div class="end-brand-name">Ember Grove</div>
        <div class="end-brand-tagline">LUXURY CANDLE MAKING KIT</div>
      </div>
    </aside>

    <section class="lid">
      <div class="hero-illustration" role="img" aria-label="Sage stipple illustration of a hand holding spa stones, bamboo and an orchid, with pastel line-drawn daisies and leaves scattered around"></div>

      <header class="brand">
        <div class="brand-name"><span class="brand-dot"></span>Ember Grove</div>
        <div class="brand-tagline">LUXURY CANDLE MAKING KIT</div>
      </header>

      <p class="features">7 Unique Candle Jars | Quality Soy Wax for 7 Candles | 7 Fragrance Oils | 16 Colors | Dried Flowers</p>

      <svg class="heart" width="18" height="16" viewBox="0 0 18 16" aria-hidden="true">
        <path d="M9 15 C3 10 0 7 0 4 A4 4 0 0 1 9 3 A4 4 0 0 1 18 4 C18 7 15 10 9 15 Z" fill="#3f6b4f"/>
      </svg>
      <p class="closing-note">hope you enjoy making it as much as<br>we enjoyed preparing it for you</p>
    </section>
  </div>
</div>
</body>
</html>
```